KWM Plumbing and Roofing

design a fresh modern card for a young plumbing business looking to break into the market.
Must include the logo in the attached file
Lowen Fairbrook
Phone number 0412689405
Vic Licence no 63920
email......

New Homes & Renovations
General Plumbing & Maintenance
Solar Hot Water Units
Roofing & Guttering (new and replacement)

Industry/Entity Type

Business

```html
<!DOCTYPE html>
<html lang="en">
<head>
<meta charset="utf-8">
<title>KWM Plumbing and Roofing – Business Card</title>
<link href="https://fonts.googleapis.com/css2?family=Source+Sans+3:wght@400;600&display=swap" rel="stylesheet">
<style>
  :root {
    --backdrop: #2b2b2b;
    --card-blue: #8fcae6;
    --pipe-blue: #1a6e9c;
    --pipe-edge: #3d8e9a;
    --brand-navy: #1d5a82;
    --ink: #111111;
    --gold-light: #f3cf6a;
    --gold-mid: #d9a634;
    --gold-dark: #a8781c;
  }
  * { margin: 0; padding: 0; box-sizing: border-box; }
  html, body {
    width: 1200px;
    height: 752px;
    overflow: hidden;
    background: var(--backdrop);
    font-family: "Source Sans 3", "Myriad Pro", Arial, sans-serif;
  }
  .card {
    position: absolute;
    top: 181px;
    width: 489px;
    height: 322px;
    background: var(--card-blue);
    overflow: hidden;
  }
  .card--front { left: 77px; }
  .card--back { left: 668px; }

  .gold-rule {
    position: absolute;
    top: 0;
    left: 458px;
    width: 12px;
    height: 100%;
    background: linear-gradient(90deg, var(--gold-dark), var(--gold-light) 45%, var(--gold-mid) 70%, var(--gold-dark));
  }

  .pipe-art {
    position: absolute;
    left: 0;
    top: 9px;
    width: 188px;
    height: 141px;
    border-radius: 0 60px 26px 0;
    background: linear-gradient(180deg, var(--pipe-blue), var(--pipe-edge));
  }

  .brand {
    position: absolute;
    left: 108px;
    top: 208px;
    display: flex;
    align-items: center;
    gap: 14px;
  }
  .brand__dot {
    width: 70px;
    height: 70px;
    border-radius: 50%;
    background: var(--brand-navy);
    flex: none;
  }
  .brand__name {
    color: var(--brand-navy);
    font-weight: 600;
    font-size: 26px;
    line-height: 1.1;
  }

  .services {
    position: absolute;
    right: 52px;
    top: 186px;
    list-style: none;
    text-align: right;
    color: var(--ink);
    font-size: 15px;
    line-height: 19.5px;
  }
  .services__phone {
    font-size: 13.5px;
    margin-top: 1px;
  }
</style>
</head>
<body>
  <section class="card card--front">
    <div class="pipe-art" role="img" aria-label="Illustration of a bent water tap pipe"></div>
    <div class="brand">
      <span class="brand__dot"></span>
      <span class="brand__name">KWM Plumbing<br>and Roofing</span>
    </div>
    <div class="gold-rule"></div>
  </section>

  <section class="card card--back">
    <ul class="services">
      <li>New Homes &amp; Renovations</li>
      <li>General Plumbing &amp; Maintenance</li>
      <li>Solar Hot Water Units</li>
      <li>Roofing &amp; Guttering (new and replacement)</li>
      <li class="services__phone">Phone number 0412689405</li>
    </ul>
    <div class="gold-rule"></div>
  </section>
</body>
</html>
```